New Alcoholic Spiked Seltzer Line

We need a can design for a line of low calorie alcoholic seltzer. This product is a sparkling water and vodka drink with no sugar added in a slim 12 oz can.

This is a lighter, healthier, alternative to the sugary ready-to-drinks on the market. The product contains only 3 ingredients: Vodka, Water and Natural Flavors. It has only 100 calories but still has 5% alcohol, so you don't need to sacrifice alcohol to cut calories.

This product also does not contain any preservatives.

We want this design to communicate the following objectives to the consumer and in this order:

1. Appetizing product
2.Low calorie
3.Communicate the type of beverage (Spiked Seltzer)

The brand name of the product is VELKA.

The flavor of the product needed to be used for the design is Mango-Orange.

Comparable products are:

www.brisavelfizz.example/
https://www.tarnowbubble.example
https://quellrind.example/

The designs should not infringe or copy the creative directions of the products mentionned above. They are only given so that you can better understand the type of product we are developing.

Target Market(s)

Young Professional women between the ages of 25 and 44

Industry/Entity Type

Product

Colors

Designer to choose colors to be used in the design.

Requirements
Must have
• Design extendibility, meaning it can be adapted for other flavors.
• This is a new category in the market we are targeting, so consumers must easily be able to identify what type of product this is.

```html
<!DOCTYPE html>
<html lang="en">
<head>
<meta charset="utf-8">
<title>Velka Spiked Seltzer – Mango-Orange Label Proposal</title>
<link rel="stylesheet" href="https://fonts.googleapis.com/css2?family=Josefin+Sans:wght@300&family=Lato:wght@300;400&display=swap">
<style>
  :root {
    --paper: #ffffff;
    --ink: #333333;
    --brick: #a33035;
    --sky: #0096d8;
    --sun: #fdca2e;
    --sun-text: #fdd530;
    --slate: #4a5b8d;
    --rule: #a6c6d2;
    --frame: #ececec;
  }
  html, body {
    margin: 0;
    padding: 0;
    width: 1200px;
    height: 849px;
    overflow: hidden;
    background: var(--paper);
  }
  .sheet { display: block; width: 1200px; height: 849px; }
  .label-frame { fill: var(--paper); stroke: var(--frame); stroke-width: 1; }
  .block-brick { fill: var(--brick); }
  .block-sun { fill: var(--sun); }
  .block-sky { fill: var(--sky); }
  .wordmark {
    font-family: "Josefin Sans", "Century Gothic", sans-serif;
    font-weight: 300;
    fill: var(--ink);
  }
  .copy {
    font-family: "Lato", "Gill Sans", sans-serif;
    font-weight: 300;
  }
  .copy-brick { fill: var(--brick); }
  .copy-slate { fill: var(--slate); }
  .copy-sun { fill: var(--sun-text); }
  .ring { fill: none; stroke: var(--ink); stroke-width: 12; }
  .rule { fill: var(--rule); }
  .proposal-title {
    font-family: "Lato", "Gill Sans", sans-serif;
    font-weight: 400;
    font-size: 16px;
    letter-spacing: 4px;
    fill: var(--ink);
  }
</style>
</head>
<body>
<svg class="sheet" viewBox="0 0 1200 849" xmlns="http://www.w3.org/2000/svg">
  <defs>
    <radialGradient id="mango-tones" cx="45%" cy="45%" r="60%">
      <stop offset="0%" stop-color="#f6b23a"/>
      <stop offset="55%" stop-color="#e4602f"/>
      <stop offset="100%" stop-color="#7aa83c"/>
    </radialGradient>
    <radialGradient id="orange-tones" cx="50%" cy="55%" r="60%">
      <stop offset="0%" stop-color="#ffd27a"/>
      <stop offset="60%" stop-color="#f7a11c"/>
      <stop offset="100%" stop-color="#e9861a"/>
    </radialGradient>
  </defs>

  <g class="label">
    <rect class="label-frame" x="180" y="48" width="840" height="608"/>

    <!-- colour blocks -->
    <rect class="block-brick" x="180" y="48" width="178" height="242"/>
    <rect class="block-sun" x="180" y="476" width="342" height="180"/>
    <rect class="block-sky" x="842" y="256" width="178" height="400"/>

    <!-- top wordmark row -->
    <text class="wordmark" x="376" y="172" font-size="112" textLength="430" lengthAdjust="spacingAndGlyphs">VELKA</text>
    <text class="copy copy-brick" x="378" y="214" font-size="32">Spiked</text>
    <text class="copy copy-brick" x="378" y="246" font-size="32">Seltzer</text>
    <text class="copy copy-slate" x="470" y="284" font-size="60" textLength="140" lengthAdjust="spacingAndGlyphs">12 oz</text>

    <!-- ingredients ring -->
    <circle class="ring" cx="932" cy="145" r="82"/>
    <text class="copy copy-brick" x="990" y="126" font-size="32" textLength="92" lengthAdjust="spacingAndGlyphs" text-anchor="end">Vodka</text>
    <text class="copy copy-brick" x="872" y="148" font-size="32" textLength="82" lengthAdjust="spacingAndGlyphs">Water</text>
    <text class="copy copy-brick" x="866" y="170" font-size="20" textLength="132" lengthAdjust="spacingAndGlyphs">Natural Flavors</text>

    <!-- middle row: alcohol ring and fruit -->
    <circle class="ring" cx="252" cy="385" r="68"/>
    <text class="copy copy-slate" x="252" y="378" font-size="36" text-anchor="middle">5%</text>
    <text class="copy copy-slate" x="252" y="412" font-size="32" textLength="100" lengthAdjust="spacingAndGlyphs" text-anchor="middle">alcohol</text>

    <g role="img" aria-label="Photo of a whole mango with a sliced wedge and green leaves">
      <circle cx="400" cy="385" r="62" fill="url(#mango-tones)"/>
      <circle class="ring" cx="400" cy="385" r="68"/>
    </g>
    <g role="img" aria-label="Photo of a whole orange with two halved oranges and leaves">
      <circle cx="548" cy="385" r="62" fill="url(#orange-tones)"/>
      <circle class="ring" cx="548" cy="385" r="68"/>
    </g>

    <!-- calories block -->
    <text class="copy copy-slate" x="188" y="526" font-size="42" textLength="324" lengthAdjust="spacingAndGlyphs">only 100 calories</text>

    <!-- vertical column -->
    <text class="wordmark" font-size="100" textLength="320" lengthAdjust="spacingAndGlyphs" transform="translate(718 640) rotate(-90)">VELKA</text>
    <text class="copy copy-brick" font-size="30" transform="translate(752 640) rotate(-90)">Spiked</text>
    <text class="copy copy-brick" font-size="30" transform="translate(778 640) rotate(-90)">Seltzer</text>
    <text class="copy copy-slate" font-size="62" textLength="320" lengthAdjust="spacingAndGlyphs" transform="translate(830 640) rotate(-90)">Low calorie</text>
    <text class="copy copy-sun" font-size="62" textLength="360" lengthAdjust="spacingAndGlyphs" transform="translate(956 636) rotate(-90)">Mango-Orange</text>
  </g>

  <g class="footer">
    <rect class="rule" x="0" y="750" width="1200" height="4"/>
    <text class="proposal-title" x="1128" y="796" text-anchor="end">PROPOSAL FOR VELKA LABEL</text>
  </g>
</svg>
</body>
</html>
```